Healthcare IT company looking for business card design

We develop IT systems for healthcare that significantly reduces cost and improves quality.

We want a business card design that is professional and clean, and using the colors in our logo.

Target Market(s)

Doctors and decision makers in the healthcare industry

Industry/Entity Type

Healthcare

Contact Information for Business Card

It should include
Name and title, address, telephone

Tobias Vrenholt, CEO
+46 712 418257
tobias@kelvaro.se

Font styles to use
Serif

Colors
0355a3
ed282f

Requirements
Must have
• Clean design
• Professional feel
Nice to have
• N/A
Should not have
• N/A

```html
<!DOCTYPE html>
<html lang="en">
<head>
<meta charset="utf-8">
<title>Kelvaro – Business Card</title>
<link rel="stylesheet" href="https://fonts.googleapis.com/css2?family=Libre+Baskerville:wght@400;700&display=swap">
<style>
  :root {
    --brand-blue: #0355a3;
    --brand-red: #ed282f;
    --card-white: #ffffff;
    --backdrop: #e9e7e3;
    --ink-soft: #2c5f93;
  }
  * { margin: 0; padding: 0; box-sizing: border-box; }
  html, body {
    width: 1200px;
    height: 1023px;
    overflow: hidden;
    background: var(--backdrop);
    font-family: "Libre Baskerville", Georgia, serif;
  }
  .canvas {
    position: relative;
    width: 1200px;
    height: 1023px;
  }
  .card {
    position: absolute;
    left: 180px;
    width: 840px;
    height: 466px;
    background: var(--card-white);
    overflow: hidden;
    box-shadow: 0 6px 22px rgba(0,0,0,0.18);
  }
  .card--front { top: 28px; }
  .card--back { top: 528px; }

  /* Front */
  .front-panel {
    position: absolute;
    left: 0; top: 0;
    width: 100%;
    height: 250px;
    background: var(--brand-blue);
  }
  .front-mark {
    position: absolute;
    left: 300px;
    top: 75px;
    width: 100px;
    height: 100px;
    border-radius: 50%;
    background: var(--card-white);
  }
  .front-stripes {
    position: absolute;
    left: 0;
    top: 250px;
    width: 300px;
    height: 216px;
  }
  .front-brand {
    position: absolute;
    right: 48px;
    top: 300px;
    display: flex;
    align-items: flex-start;
    gap: 10px;
  }
  .front-brand__square {
    width: 22px;
    height: 22px;
    background: var(--brand-red);
    margin-top: 4px;
  }
  .front-brand__name {
    font-weight: 700;
    font-size: 104px;
    line-height: 1;
    color: var(--brand-blue);
    letter-spacing: -1px;
  }

  /* Back */
  .back-stripes {
    position: absolute;
    right: 0;
    top: 0;
    width: 300px;
    height: 466px;
  }
  .contact {
    position: absolute;
    left: 64px;
    top: 150px;
    color: var(--brand-blue);
  }
  .contact__name {
    font-size: 34px;
    font-weight: 700;
    margin-bottom: 8px;
  }
  .contact__title {
    font-size: 18px;
    letter-spacing: 2px;
    color: var(--ink-soft);
    margin-bottom: 40px;
  }
  .contact__line {
    font-size: 20px;
    line-height: 1.7;
  }
</style>
</head>
<body>
<main class="canvas">
  <section class="card card--front" aria-label="Business card front">
    <div class="front-panel"></div>
    <div class="front-mark"></div>
    <svg class="front-stripes" viewBox="0 0 300 216" aria-hidden="true">
      <rect x="40" y="0" width="14" height="216" fill="#0355a3"/>
      <rect x="74" y="0" width="8" height="216" fill="#0355a3"/>
      <rect x="102" y="0" width="22" height="216" fill="#0355a3"/>
      <rect x="150" y="0" width="44" height="216" fill="#0355a3"/>
    </svg>
    <div class="front-brand">
      <span class="front-brand__square"></span>
      <span class="front-brand__name">Kelvaro</span>
    </div>
  </section>

  <section class="card card--back" aria-label="Business card back">
    <div class="contact">
      <p class="contact__name">Tobias Vrenholt</p>
      <p class="contact__title">CEO</p>
      <p class="contact__line">+46 712 418257</p>
      <p class="contact__line">tobias@kelvaro.se</p>
    </div>
    <svg class="back-stripes" viewBox="0 0 300 466" aria-hidden="true">
      <rect x="60" y="0" width="44" height="466" fill="#0355a3"/>
      <rect x="130" y="0" width="22" height="466" fill="#0355a3"/>
      <rect x="172" y="0" width="8" height="466" fill="#0355a3"/>
      <rect x="202" y="0" width="14" height="466" fill="#0355a3"/>
    </svg>
  </section>
</main>
</body>
</html>
```